Real Estate 24"x24" Sign, Business Card, Letter Head and Envelope

This is a 4 project contest. If we choose a design or designs we like from what you sent we are willing to pay an amount at our discretion for that design even if we don't like all your designs for the 4 projects. Please be creative. Attached are our logo files. Please message us with any questions. Thanks and Good Luck!
Project 1: QLTV Realty 24" x 24" yard sign
We want to use the same blue background in our logo for the sign where the logo in white font will be on. CMYK 100,80,0,0. Attached is a sample a local designer made for you to get an idea what we are looking for. In the sample, the website is way too big and the entire sign is very plain and not attractive looking plus blue color is wrong one. We want the logo on top as large as possible but keeping it proportionate and attractive looking buy not too big that it looks odd. The following information can go in white color background or same blue color background color. Our company colors are blue (as per logo), green (as per logo), and white. "Residential & Commercial" goes under the logo. Under that put our phone number "312-948-6051" as large as possible but still looks good and under that our website in much smaller but readable font "www.qltvrealty.com".
Project 2: Envelope
We have two version of the logo. Use one or both. Whatever looks best in your design. The envelope will be white. We only want on top left corner logo and underneath our mailing address: 5197 Larchmere Ave. Larchfield, OH 60093-1725. Maybe some creative decorative design at bottom of envelope will look nice
Project 3: Letter Head
We have two version of the logo. Use one or both. Whatever looks best in your design. We want the following information on the top of the letterhead. Logo, address: 5197 Larchmere Ave., Larchfield, OH 60093-1725, phone: 312-948-6051, fax: 312-682-9307 website www.qltvrealty.com, email: info@qltvrealty.com
Project 4: Business card
Use either logo. We need cards for two individuals. Information for Person 1: Dev Kulkarni, Managing Broker, Phone: 312-948-6051, Email: dev.kulkarni@qltvrealty.com. Person 2: Ajay Kulkarni Broker Phone: 312-519-8263 Email: ajay.kulkarni@qltvrealty.com. Add Address, Fax and website same as above letter head.

```html
<!DOCTYPE html>
<html lang="en">
<head>
<meta charset="utf-8">
<title>QLTV Realty Stationery</title>
<link href="https://fonts.googleapis.com/css2?family=Roboto:wght@400;500;700&family=Questrial&display=swap" rel="stylesheet">
<style>
  :root {
    --brand-blue: #1a4fa3;
    --brand-green: #76c143;
    --ink: #555a60;
    --ink-soft: #7b8087;
    --paper: #ffffff;
    --paper-warm: #f7f7f7;
    --backdrop: #dedede;
    --rule: #c9cdd2;
  }
  * { margin: 0; padding: 0; box-sizing: border-box; }
  html, body { width: 1200px; height: 649px; overflow: hidden; }
  body {
    position: relative;
    background: var(--backdrop);
    font-family: "Roboto", Arial, sans-serif;
    color: var(--ink);
  }
  .sheet {
    position: absolute;
    background: var(--paper);
    box-shadow: 0 2px 6px rgba(0,0,0,.18);
    overflow: hidden;
  }
  .stripe-top { position: absolute; left: 0; right: 0; top: 0; height: 3px; background: var(--brand-green); }
  .stripe-bottom { position: absolute; left: 0; right: 0; bottom: 0; height: 3px; background: var(--brand-blue); }

  /* wordmark: company name set in the text face */
  .wordmark {
    position: absolute;
    font-family: "Roboto", Arial, sans-serif;
    font-weight: 700;
    color: var(--brand-blue);
    line-height: 1;
    white-space: nowrap;
  }
  .wordmark.on-green { color: var(--paper); }

  /* business cards */
  .card { left: 68px; width: 221px; height: 126px; }
  .card-front-1 { top: 187px; }
  .card-front-2 { top: 330px; }
  .card-back { top: 470px; background: var(--brand-green); }
  .card .wordmark { left: 18px; top: 57px; font-size: 14px; }
  .card-divider { position: absolute; left: 114px; top: 30px; width: 1px; height: 72px; background: var(--rule); }
  .card-details { position: absolute; left: 126px; top: 30px; font-size: 6px; line-height: 7.6px; }
  .card-name { font-size: 8.5px; font-weight: 700; color: var(--brand-blue); text-transform: uppercase; line-height: 10px; }
  .card-title { font-size: 6px; font-weight: 500; color: var(--brand-green); text-transform: uppercase; margin-bottom: 4px; }
  .card-address { margin-bottom: 3px; }
  .contact-line { display: flex; align-items: center; gap: 4px; }
  .contact-line svg { width: 5px; height: 5px; fill: var(--brand-blue); flex: none; }
  .card-back .wordmark { left: 0; right: 0; top: 52px; text-align: center; font-size: 20px; }
  .card-back-web { position: absolute; left: 0; right: 0; top: 108px; text-align: center; color: var(--paper); font-size: 6px; letter-spacing: 1.6px; }

  /* letterhead */
  .letterhead { left: 315px; top: 46px; width: 391px; height: 550px; background: var(--paper-warm); }
  .letterhead .stripe-top, .letterhead .stripe-bottom { height: 4px; }
  .letterhead .wordmark { left: 35px; top: 72px; font-size: 22px; }
  .letterhead-divider { position: absolute; left: 286px; top: 34px; width: 1px; height: 46px; background: var(--rule); }
  .letterhead-contact { position: absolute; left: 294px; top: 33px; font-size: 5.6px; line-height: 7.4px; }
  .letterhead-contact .address { margin-bottom: 2px; }
  .letter-body { position: absolute; left: 35px; top: 156px; width: 326px; font-family: "Questrial", Arial, sans-serif; }
  .salutation { font-size: 9.5px; color: #4a4f55; margin-bottom: 20px; }
  .letter-body p.copy { font-size: 5.5px; line-height: 8.4px; color: var(--ink-soft); margin-bottom: 9px; text-align: justify; }
  .closing { font-size: 5.4px; color: var(--ink-soft); margin-top: 20px; }
  .signature { position: absolute; left: 35px; top: 384px; width: 72px; height: 28px; background: linear-gradient(90deg, rgba(26,79,163,.22), rgba(26,79,163,.08)); border-radius: 3px; }
  .letterhead-web { position: absolute; left: 0; right: 0; top: 531px; text-align: center; font-size: 6px; letter-spacing: 1.8px; color: var(--ink-soft); }

  /* envelopes */
  .envelope { left: 733px; width: 393px; }
  .envelope-back { top: 198px; height: 179px; }
  .envelope-flap { position: absolute; left: 0; top: 0; width: 393px; height: 60px; }
  .envelope-back .wordmark { left: 0; right: 0; top: 24px; text-align: center; font-size: 14px; }
  .envelope-front { top: 415px; height: 180px; }
  .envelope-front .stripe-top, .envelope-front .stripe-bottom { height: 4px; }
  .envelope-front .wordmark { left: 21px; top: 44px; font-size: 15px; }
  .return-address { position: absolute; left: 21px; top: 73px; font-size: 5.8px; line-height: 7.4px; }
</style>
</head>
<body>
<svg width="0" height="0" style="position:absolute" aria-hidden="true">
  <symbol id="icon-phone" viewBox="0 0 10 10"><path d="M2 0.5l2 2-1 1.3c.6 1.3 1.7 2.4 3 3l1.3-1 2 2-1.3 1.7C4.6 9.2.8 5.4.3 1.8z"/></symbol>
  <symbol id="icon-fax" viewBox="0 0 10 10"><rect x="2.5" y="0.5" width="5" height="3"/><rect x="0.5" y="3.8" width="9" height="4.2" rx="1"/><rect x="2.5" y="7" width="5" height="2.5"/></symbol>
  <symbol id="icon-mail" viewBox="0 0 10 10"><path d="M0.5 2h9v6h-9z M0.8 2.3L5 5.6 9.2 2.3" stroke="#fff" stroke-width=".6"/></symbol>
  <symbol id="icon-web" viewBox="0 0 10 10"><circle cx="5" cy="5" r="4.5"/><path d="M0.5 5h9M5 .5c-2 2.5-2 6.5 0 9M5 .5c2 2.5 2 6.5 0 9" stroke="#fff" stroke-width=".6" fill="none"/></symbol>
</svg>

<!-- business card: managing broker -->
<section class="sheet card card-front-1">
  <div class="stripe-top"></div>
  <div class="wordmark">QLTV Realty</div>
  <div class="card-divider"></div>
  <div class="card-details">
    <div class="card-name">Dev Kulkarni</div>
    <div class="card-title">Managing Broker</div>
    <div>5197 Larchmere Ave.</div>
    <div class="card-address">Larchfield, OH 60093-1725</div>
    <div class="contact-line"><svg><use href="#icon-phone"/></svg>312-948-6051</div>
    <div class="contact-line"><svg><use href="#icon-fax"/></svg>312-682-9307</div>
    <div class="contact-line"><svg><use href="#icon-mail"/></svg>dev.kulkarni@qltvrealty.com</div>
    <div class="contact-line"><svg><use href="#icon-web"/></svg>www.qltvrealty.com</div>
  </div>
  <div class="stripe-bottom"></div>
</section>

<!-- business card: broker -->
<section class="sheet card card-front-2">
  <div class="stripe-top"></div>
  <div class="wordmark">QLTV Realty</div>
  <div class="card-divider"></div>
  <div class="card-details">
    <div class="card-name">Ajay Kulkarni</div>
    <div class="card-title">Broker</div>
    <div>5197 Larchmere Ave.</div>
    <div class="card-address">Larchfield, OH 60093-1725</div>
    <div class="contact-line"><svg><use href="#icon-phone"/></svg>312-519-8263</div>
    <div class="contact-line"><svg><use href="#icon-fax"/></svg>312-682-9307</div>
    <div class="contact-line"><svg><use href="#icon-mail"/></svg>ajay.kulkarni@qltvrealty.com</div>
    <div class="contact-line"><svg><use href="#icon-web"/></svg>www.qltvrealty.com</div>
  </div>
  <div class="stripe-bottom"></div>
</section>

<!-- business card: back -->
<section class="sheet card card-back">
  <div class="wordmark on-green">QLTV Realty</div>
  <div class="card-back-web">www.qltvrealty.com</div>
</section>

<!-- letterhead -->
<section class="sheet letterhead">
  <div class="stripe-top"></div>
  <div class="wordmark">QLTV Realty</div>
  <div class="letterhead-divider"></div>
  <div class="letterhead-contact">
    <div class="address">5197 Larchmere Ave.<br>Larchfield, OH 60093-1725</div>
    <div class="contact-line"><svg><use href="#icon-phone"/></svg>312-948-6051</div>
    <div class="contact-line"><svg><use href="#icon-fax"/></svg>312-682-9307</div>
    <div class="contact-line"><svg><use href="#icon-mail"/></svg>info@qltvrealty.com</div>
  </div>
  <div class="letter-body">
    <div class="salutation">Dear Mr. Harlow,</div>
    <p class="copy">Lorem ipsum dolor sit amet, consectetur adipiscing elit. Donec orci purus, luctus vitae dignissim eu, iaculis sed purus. Vivamus faucibus, ipsum nec aliquet viverra, leo mauris condimentum ligula, sit amet sagittis enim ligula quis arcu. Nam egestas tortor id nisi porttitor mattis. In tortor ante, ultricies in suscipit a, tempus non massa. Vivamus et auctor mi. Fusce vel massa nulla. Phasellus nec eros mauris, et scelerisque orci.</p>
    <p class="copy">Donec malesuada orci vitae nulla accumsan porta a id massa. Quisque accumsan iaculis magna sit amet fringilla. Maecenas consequat, magna eget tincidunt semper, odio nibh rutrum mi, id feugiat ante nisi eu risus. Vestibulum nunc orci, rhoncus a placerat in, ultricies in mi. Cras mattis varius eros, vel fringilla nisi suscipit eget. Quisque scelerisque sagittis nulla at porttitor.</p>
    <p class="copy">Sed id augue vitae urna euismod commodo aliquet a quam. Pellentesque arcu velit, cursus et malesuada ut, consequat et diam. Nullam erat sem, rhoncus id ullamcorper vitae, rhoncus et arcu. In ultricies ultricies nulla, ut rutrum nisi iaculis at. Donec eu magna a metus ornare faucibus. Fusce aliquet faucibus ultricies. Morbi semper, est id tincidunt gravida, sem arcu adipiscing lacus, ac bibendum nulla leo eu purus. Quisque nec diam sed risus consectetur accumsan quis quis nibh. Vestibulum id purus lorem.</p>
    <p class="copy">It is a long established fact that a reader will be distracted by the readable content of a page when looking at its layout. The point of using Lorem Ipsum is that it has a more-or-less normal distribution of letters, as opposed to using 'Content here, content here', making it look like readable English. Many desktop publishing packages</p>
    <div class="closing">Sincerely,</div>
  </div>
  <div class="signature" role="img" aria-label="Handwritten signature of the sender"></div>
  <div class="letterhead-web">www.qltvrealty.com</div>
  <div class="stripe-bottom"></div>
</section>

<!-- envelope back with flap -->
<section class="sheet envelope envelope-back">
  <svg class="envelope-flap" viewBox="0 0 393 60" preserveAspectRatio="none" aria-hidden="true">
    <path d="M0 0H393V28Q393 56 360 56H33Q0 56 0 28Z" fill="#76c143"/>
  </svg>
  <div class="wordmark on-green">QLTV Realty</div>
</section>

<!-- envelope front -->
<section class="sheet envelope envelope-front">
  <div class="stripe-top"></div>
  <div class="wordmark">QLTV Realty</div>
  <div class="return-address">5197 Larchmere Ave.<br>Larchfield, OH 60093-1725</div>
  <div class="stripe-bottom"></div>
</section>
</body>
</html>
```